"9" length 6.5" height" post card of pennyvault.net trying to get people to text the word YES to our phone number to access our latest stock picks. or tickerleaf.io we own both of them. Call to action. Get winnin stock picks sign up now text the word "YES" to 888-412-7390. must haves: " track record 2023: 477.8%" "#1 stock picking newsletter in the U.S.A." " Disclaimer: The materials and content provided by PennyVault.net, including but not limited to our website, emails, blogs, and text messages (collectively, the "Materials"), are intended for general information purposes only and do not constitute financial, legal, or investment advice. PennyVault.net is engaged in the business of marketing and advertising companies for compensation. The information contained in the Materials is not, and should not be read as, an offer or recommendation to buy or sell any securities. All content is provided for informational and educational purposes only. PennyVault.net and its staff are not licensed investment advisors, brokers, or dealers. Any content provided by us is not intended to solicit or recommend any investment and should not be used as the basis for any investment decisions. We do not provide investment advice, endorse any financial product, or suggest that any particular investment or strategy is suitable for any specific person. PennyVault.net receives compensation from the companies featured in our alerts, emails, and other Materials for marketing and advertising services. The existence of such compensation may influence the content, topics, or posts made in the Materials. Investing in stocks, especially penny stocks, involves a high level of risk and may not be suitable for all investors. The possibility exists that you could sustain a loss of some or all of your initial investment. Therefore, you should not invest money that you cannot afford to lose. The performance figures stated in the Materials, including but not limited to a track record of 477% in 2023, are hypothetical and should not be considered indicative of future results. Past performance is not necessarily indicative of future results. Individual results may vary, and the examples used in the Materials are not guaranteed to occur. You are encouraged to perform your own due diligence and consult with a qualified financial advisor before making any investment decisions. PennyVault.net and its Materials should not be used as the sole basis for any investment decision. We make no representation or warranty as to the accuracy, completeness, or reliability of the information contained in the Materials. The content provided by PennyVault.net and in its newsletter is intended for entertainment purposes only. Acknowledgment: By using PennyVault.net's services, joining our site, or subscribing to our email/blog list, you acknowledge that you have read, understood, and agree to be bound by the terms of this disclaimer. If you do not agree with these terms, you should not use our services or subscribe to our Materials

."

Target Market(s)

investors

Industry/Entity Type

financial

Colors
0054AA
0677BA
7BADD7
CADEEF
E8F1F8
00AB8E
00BBA5
67D7C9
C6EFE9
E9F9F6
59FF00
82FF00
B8FF75
E3FFCB
F4FFEA

Requirements
Must have
• " track record 2023: 477.8%" "#1 stock picking newsletter in the U.S.A." "Disclaimer: The materials and content provided by PennyVault.net, including but not limited to our website, emails, blogs, and text messages (collectively, the "Materials"), are intended for general information purposes only and do not constitute financial, legal, or investment advice. PennyVault.net is engaged in the business of marketing and advertising companies for compensation. The information contained in the Materials is not, and should not be read as, an offer or recommendation to buy or sell any securities. All content is provided for informational and educational purposes only. PennyVault.net and its staff are not licensed investment advisors, brokers, or dealers. Any content provided by us is not intended to solicit or recommend any investment and should not be used as the basis for any investment decisions. We do not provide investment advice, endorse any financial product, or suggest that any particular investment or strategy is suitable for any specific person. PennyVault.net receives compensation from the companies featured in our alerts, emails, and other Materials for marketing and advertising services. The existence of such compensation may influence the content, topics, or posts made in the Materials. Investing in stocks, especially penny stocks, involves a high level of risk and may not be suitable for all investors. The possibility exists that you could sustain a loss of some or all of your initial investment. Therefore, you should not invest money that you cannot afford to lose. The performance figures stated in the Materials, including but not limited to a track record of 477% in 2023, are hypothetical and should not be considered indicative of future results. Past performance is not necessarily indicative of future results. Individual results may vary, and the examples used in the Materials are not guaranteed to occur. You are encouraged to perform your own due diligence and consult with a qualified financial advisor before making any investment decisions. PennyVault.net and its Materials should not be used as the sole basis for any investment decision. We make no representation or warranty as to the accuracy, completeness, or reliability of the information contained in the Materials. The content provided by PennyVault.net and in its newsletter is intended for entertainment purposes only. Acknowledgment: By using PennyVault.net's services, joining our site, or subscribing to our email/blog list, you acknowledge that you have read, understood, and agree to be bound by the terms of this disclaimer. If you do not agree with these terms, you should not use our services or subscribe to our Materials."
Nice to have
• call to action: Get exclusive stock picks delivered directly to your phone. Text "YES" to [888-412-7390] to receive your first stock pick

```html
<!DOCTYPE html>
<html lang="en">
<head>
<meta charset="utf-8">
<title>PennyVault.net Postcard</title>
<link rel="stylesheet" href="https://fonts.googleapis.com/css2?family=Montserrat:ital,wght@0,500;0,700;0,800;0,900;1,900&family=Oswald:wght@500;600&family=Roboto+Condensed:wght@400;700&family=Poppins:wght@400;500;600&display=swap">
<style>
:root{
  --navy:#0b1a8a;
  --navy-mid:#1233b5;
  --blue:#0054AA;
  --teal:#00BBA5;
  --teal-dark:#00AB8E;
  --teal-light:#67D7C9;
  --green:#59FF00;
  --green-mid:#82FF00;
  --green-deep:#3cb800;
  --ink:#0b2a8f;
  --white:#ffffff;
  --stage:#ececec;
}
*{box-sizing:border-box;margin:0;padding:0}
html,body{width:1200px;height:2234px;overflow:hidden;background:var(--stage)}
body{position:relative;font-family:"Montserrat",sans-serif;color:var(--white)}
.card{position:absolute;left:40px;width:1120px;height:788px;overflow:hidden;box-shadow:0 12px 30px rgba(0,0,0,.28)}
.card--front{top:215px}
.card--back{top:1230px;background:var(--white)}
.abs{position:absolute}

/* front */
.hero{left:0;top:0;width:1120px;height:400px;background:radial-gradient(ellipse at 85% 30%,#1b86d8 0%,rgba(27,134,216,0) 45%),linear-gradient(120deg,var(--navy) 0%,var(--navy-mid) 55%,#0a58c0 100%)}
.hero__glow{left:0;top:250px;width:420px;height:150px;background:linear-gradient(90deg,rgba(230,110,40,.45),rgba(120,40,160,.15) 70%,rgba(0,0,0,0))}
.rank{left:70px;top:40px;font-family:"Oswald",sans-serif;font-weight:600;font-size:220px;line-height:190px;color:var(--teal);letter-spacing:-6px;transform:scaleX(.68);transform-origin:left top}
.headline{left:236px;top:40px;font-weight:800;font-size:60px;line-height:63px;letter-spacing:.5px;text-transform:uppercase}
.track-label{left:71px;top:264px;font-weight:500;font-size:29px;letter-spacing:.5px}
.track-year{left:68px;top:290px;font-weight:800;font-size:80px;line-height:1;letter-spacing:1px}
.track-pill{left:325px;top:270px;width:356px;height:93px;border-radius:14px;background:linear-gradient(180deg,var(--green-mid),var(--green) 55%,var(--green-deep));box-shadow:inset 0 0 0 3px rgba(255,255,255,.35);color:var(--ink);font-weight:900;font-style:italic;font-size:82px;line-height:93px;text-align:center;letter-spacing:1px}
.legal{left:0;top:400px;width:1120px;height:294px;background:linear-gradient(180deg,var(--teal) 0%,#00c9b0 100%)}
.legal__title{left:70px;top:418px;font-weight:700;font-size:18px}
.legal__body{left:70px;top:446px;width:690px;font-family:"Roboto Condensed",sans-serif;font-size:10px;line-height:13.6px;text-align:justify}
.phone{left:764px;top:73px;width:270px;height:552px;border-radius:40px;border:7px solid #2b2f38;background:linear-gradient(180deg,#1d5fb0 0%,#7fa7d0 40%,#b9c9d8 100%);box-shadow:0 16px 30px rgba(0,0,0,.35)}

/* cta band */
.cta{left:0;top:694px;width:1120px;height:94px;background:linear-gradient(90deg,var(--navy) 0%,var(--navy-mid) 60%,#1446c8 100%)}
.cta--back{top:698px;height:90px}
.cta__pitch{left:46px;top:18px;font-family:"Oswald",sans-serif;font-weight:500;font-size:23px;line-height:27px;text-transform:uppercase}
.cta__text{left:325px;top:30px;font-weight:700;font-size:26px}
.cta__yes{color:var(--green)}
.cta__number{left:513px;top:15px;width:382px;height:62px;border-radius:31px;background:linear-gradient(180deg,var(--green-mid),var(--green) 55%,var(--green-deep));box-shadow:inset 0 0 0 3px rgba(255,255,255,.35);color:var(--ink);font-weight:800;font-size:44px;line-height:62px;text-align:center;letter-spacing:1px}
.cta--back .cta__number{top:13px}
.cta__tail{left:911px;top:18px;font-weight:700;font-size:21px;line-height:27px}

/* back */
.terms{left:0;top:0;width:731px;height:445px;background:linear-gradient(120deg,var(--navy) 0%,var(--navy-mid) 65%,#0a58c0 100%)}
.terms__col{top:38px;width:312px;font-family:"Poppins",sans-serif;font-size:9.7px;line-height:14.4px;text-align:justify}
.terms__col--left{left:44px}
.terms__col--right{left:378px;width:310px}
.terms__heading{font-family:"Montserrat",sans-serif;font-weight:700;font-size:11px;line-height:14px;margin-bottom:4px}
.terms__para{margin-bottom:18px}
.terms__note{left:44px;top:404px;font-family:"Poppins",sans-serif;font-size:9.7px;line-height:14px;width:600px}
.perks{left:0;top:445px;width:731px;height:253px;background:linear-gradient(180deg,var(--teal) 0%,#00c9b0 100%)}
.ack{left:44px;top:462px;width:312px;font-family:"Poppins",sans-serif;font-size:9.7px;line-height:14.4px;text-align:justify}
.visit{left:44px;top:575px;font-family:"Poppins",sans-serif;font-size:20px}
.visit__url{left:44px;top:608px;width:310px;height:34px;border-radius:17px;background:var(--white);color:var(--blue);font-weight:700;font-size:20px;line-height:34px;text-align:center}
.visit__after{left:44px;top:651px;font-family:"Poppins",sans-serif;font-size:16px}
.bullets{left:390px;top:472px;width:320px;list-style:none;font-family:"Poppins",sans-serif;font-size:17px;line-height:22px}
.bullets li{position:relative;padding-left:22px;margin-bottom:12px}
.bullets li::before{content:"";position:absolute;left:2px;top:8px;width:8px;height:8px;border-radius:50%;background:var(--green)}
.indicia{left:1003px;top:28px;width:90px;height:87px;border:1.5px solid #222;color:#111;font-family:"Roboto Condensed",sans-serif;font-weight:700;font-size:12px;line-height:14.5px;text-align:center;padding-top:7px}
.address{left:812px;top:144px;width:284px;height:92px;border:1.5px solid #222;color:#111;font-family:"Roboto Condensed",sans-serif;font-size:17px;line-height:22px;padding:10px 0 0 22px}
.address__route{display:block;text-align:center;padding-right:22px}
</style>
</head>
<body>

<section class="card card--front">
  <div class="abs hero"></div>
  <div class="abs hero__glow" role="img" aria-label="Soft candlestick stock chart glow behind the headline"></div>
  <div class="abs rank">#1</div>
  <h1 class="abs headline">Stock Picking<br>Newsletter<br>In the U.S.A</h1>
  <div class="abs track-label">TRACK RECORD</div>
  <div class="abs track-year">2023</div>
  <div class="abs track-pill">477.8%</div>

  <div class="abs legal"></div>
  <div class="abs legal__title">Disclaimer:</div>
  <p class="abs legal__body">The materials and content provided by PennyVault.net, including but not limited to our website, emails, blogs, and text messages (collectively, the "Materials"), are intended for general information purposes only and do not constitute financial, legal, or investment advice. PennyVault.net is engaged in the business of marketing and advertising companies for compensation. The information contained in the Materials is not, and should not be read as, an offer or recommendation to buy or sell any securities. All content is provided for informational and educational purposes only. PennyVault.net and its staff are not licensed investment advisors, brokers, or dealers. Any content provided by us is not intended to solicit or recommend any investment and should not be used as the basis for any investment decisions. We do not provide investment advice, endorse any financial product, or suggest that any particular investment or strategy is suitable for any specific person. PennyVault.net receives compensation from the companies featured in our alerts, emails, and other Materials for marketing and advertising services. The existence of such compensation may influence the content, topics, or posts made in the Materials. Investing in stocks, especially penny stocks, involves a high level of risk and may not be suitable for all investors. The possibility exists that you could sustain a loss of some or all of your initial investment. Therefore, you should not invest money that you cannot afford to lose. The performance figures stated in the Materials, including but not limited to a track record of 477% in 2023, are hypothetical and should not be considered indicative of future results. Past performance is not necessarily indicative of future results. Individual results may vary, and the examples used in the Materials are not guaranteed to occur. You are encouraged to perform your own due diligence and consult with a qualified financial advisor before making any investment decisions. PennyVault.net and its Materials should not be used as the sole basis for any investment decision. We make no representation or warranty as to the accuracy, completeness, or reliability of the information contained in the Materials. The content provided by PennyVault.net and in its newsletter is intended for entertainment purposes only. Acknowledgment: By using PennyVault.net's services, joining our site, or subscribing to our email/blog list, you acknowledge that you have read, understood, and agree to be bound by the terms of this disclaimer. If you do not agree with these terms, you should not use our services or subscribe to our Materials</p>

  <div class="abs phone" role="img" aria-label="Smartphone lock screen showing a text message alert with the day's stock pick"></div>

  <div class="abs cta">
    <div class="abs cta__pitch">Get exclusive stock picks<br>delivered to your phone.</div>
    <div class="abs cta__text">Text "<span class="cta__yes">YES</span>" to</div>
    <div class="abs cta__number">888-412-7390</div>
    <div class="abs cta__tail">to receive your<br>first stock pick</div>
  </div>
</section>

<section class="card card--back">
  <div class="abs terms"></div>
  <div class="abs terms__col terms__col--left">
    <h3 class="terms__heading">Not Investment Advice</h3>
    <p class="terms__para">The materials and content provided by PennyVault.net, including but not limited to our website, emails, blogs, and text messages (collectively, the "Materials"), are intended for general information purposes only and do not constitute financial, legal, or investment advice. PennyVault.net is engaged in the business of marketing and advertising companies for compensation. The information contained in the Materials is not, and should not be read as, an offer or recommendation to buy or sell any securities. All content is provided for informational and educational purposes only.</p>
    <h3 class="terms__heading">Risk Acknowledgment and Investment Performance</h3>
    <p class="terms__para">The materials and content provided by PennyVault.net, including but not limited to our website, emails, blogs, and text messages (collectively, the "Materials"), are intended for general information purposes only and do not constitute financial, legal, or investment advice. PennyVault.net is engaged in the business of marketing and advertising companies for compensation. The information contained in the Materials is not, and should not be read as, an offer or recommendation to buy or sell any securities. All content is provided for informational and educational purposes only.</p>
  </div>
  <div class="abs terms__col terms__col--right">
    <h3 class="terms__heading">No Licensing</h3>
    <p class="terms__para">PennyVault.net and its staff are not licensed investment advisors, brokers, or dealers. Any content provided by us is not intended to solicit or recommend any investment and should not be used as the basis for any investment decisions. We do not provide investment advice, endorse any financial product, or suggest that any particular investment or strategy is suitable for any specific person.</p>
    <h3 class="terms__heading">Compensation Disclosure</h3>
    <p class="terms__para">PennyVault.net receives compensation from the companies featured in our alerts, emails, and other Materials for marketing and advertising services. The existence of such compensation may influence the content, topics, or posts made in the Materials.</p>
    <h3 class="terms__heading">Due Diligence and Professional Advice</h3>
    <p class="terms__para">You are encouraged to perform your own due diligence and consult with a qualified financial advisor before making any investment decisions. PennyVault.net and its Materials should not be used as the sole basis for any investment decision. We make no representation or warranty as to the accuracy, completeness, or reliability of the information contained in the Materials.</p>
  </div>
  <div class="abs terms__note">
    <h3 class="terms__heading">Entertainment Purposes Only</h3>
    <p>The content provided by PennyVault.net and in its newsletter is intended for entertainment purposes only.</p>
  </div>

  <div class="abs perks"></div>
  <div class="abs ack">
    <h3 class="terms__heading">Acknowledgment</h3>
    <p>By using PennyVault.net's services, joining our site, or subscribing to our email/blog list, you acknowledge that you have read, understood, and agree to be bound by the terms of this disclaimer. If you do not agree with these terms, you should not use our services or subscribe to our Materials.</p>
  </div>
  <div class="abs visit">Visit</div>
  <div class="abs visit__url">PennyVault.net/disclaimer</div>
  <div class="abs visit__after">for full disclaimer and terms of use.</div>
  <ul class="abs bullets">
    <li>2023 Track Record: 477.2%.</li>
    <li>2024 Track Record: 88.3%.</li>
    <li>28 of Last 35 Trades Won!</li>
    <li>Make BIG Money Following Our Trades.</li>
    <li>Apply Now to see if you qualify for our service.</li>
  </ul>

  <div class="abs indicia">PRSRT STD<br>ECRWSS<br>U.S. POSTAGE<br>PAID<br>EDDM RETAIL</div>
  <div class="abs address"><span class="address__route">*********ECRWSS*********</span>Local<br>Postal Customer</div>

  <div class="abs cta cta--back">
    <div class="abs cta__pitch">Get exclusive stock picks<br>delivered to your phone.</div>
    <div class="abs cta__text">Text "<span class="cta__yes">YES</span>" to</div>
    <div class="abs cta__number">888-412-7390</div>
    <div class="abs cta__tail">to receive your<br>first stock pick</div>
  </div>
</section>

</body>
</html>
```